I need a wordpress website for myconsulting company specialized in data privacy

I'm looking for a wordpress website for my consulting company specialized in data privacy (GDPR) and computer science.
The website will serve as entry point to for potential clients.
The website should have the following sections (I'm opened to new ideas):
- Presentation of the company
- General presentation
- Services provided with some details
- Blog/articles with tags (if possible)
- Contact
On every page of the website there should be some references to pages (such as privacy policy, legal information...)
If possible he website should be multinlingual (english and french). I'll personnally take care of the translation in french.
Regarding branding;
- Name of the company: Laurent Dubreuil Conseil
- Logo is attached
- For colors to be used see attached PDF for exemple

```html
<!DOCTYPE html>
<html lang="en">
<head>
<meta charset="utf-8">
<title>Laurent Dubreuil Conseil — Data Privacy &amp; Computer Science</title>
<link rel="stylesheet" href="https://fonts.googleapis.com/css2?family=Krona+One&family=Montserrat:wght@400;500&family=Barlow+Condensed:wght@500;600&display=swap">
<style>
:root{
  --teal:#0f8b96;
  --teal-dark:#0a7580;
  --navy:#0b1b2e;
  --ink:#0f1b2b;
  --text:#3b4656;
  --soft:#eaeff7;
  --white:#ffffff;
}
*{box-sizing:border-box;margin:0;padding:0}
html,body{width:1200px;height:3636px;overflow:hidden}
body{position:relative;background:var(--white);font-family:"Montserrat",sans-serif;color:var(--text)}
.abs{position:absolute}
.display{font-family:"Krona One",sans-serif;color:var(--ink);font-weight:400;letter-spacing:1px}
.accent{color:var(--teal)}
.cond{font-family:"Barlow Condensed",sans-serif;font-weight:600}
.btn{position:absolute;display:flex;align-items:center;justify-content:center;background:var(--teal);color:var(--white);font-family:"Barlow Condensed",sans-serif;font-weight:600;font-size:16px;border-radius:4px;text-decoration:none}
.stack{position:absolute;display:flex;flex-direction:column;align-items:flex-start}
.stack .btn{position:static}
.brand{display:flex;align-items:center;gap:8px;font-family:"Montserrat",sans-serif;font-weight:500;font-size:15px;color:var(--ink)}
.brand-mark{width:18px;height:18px;background:var(--teal);border-radius:3px}

/* header + hero */
.hero{position:absolute;left:0;top:0;width:1200px;height:541px;background:linear-gradient(110deg,#f3f5fb 0%,#eceff8 55%,#e2e7f4 100%);overflow:hidden}
.hero-arc{position:absolute;left:420px;top:-60px;width:900px;height:700px;border-radius:50%;background:rgba(220,226,242,.6)}
.nav{position:absolute;top:26px;left:513px;font-family:"Barlow Condensed",sans-serif;font-weight:500;font-size:15px;color:var(--ink)}
.nav a{position:absolute;white-space:nowrap;text-decoration:none;color:inherit}
.nav .active{color:var(--teal);border-bottom:2px solid var(--teal);padding-bottom:4px}
.phone{display:flex;align-items:center;gap:6px;color:var(--teal)!important;font-weight:600}
.hero-art{position:absolute;left:630px;top:55px;width:560px;height:440px;border-radius:40% 45% 40% 50%;background:radial-gradient(circle at 45% 45%,#c8b7f4 0%,#d9d0f7 30%,#e6e9f6 65%,rgba(230,233,246,0) 80%)}
.slider{position:absolute;left:163px;top:502px;display:flex;align-items:center;gap:6px;font-family:"Barlow Condensed",sans-serif;font-weight:600}
.slider .line{width:148px;height:1px;background:var(--teal)}

/* paragraphs */
.copy{font-size:13.8px;line-height:22.5px;letter-spacing:-.15px;color:var(--text)}

/* sections */
.band-soft{position:absolute;left:0;width:1200px;background:var(--soft)}
.photo{position:absolute}

.ticks{list-style:none}
.ticks li{display:flex;align-items:center;gap:10px;font-size:13.8px;letter-spacing:-.15px;height:28.5px;color:var(--ink)}

.card{position:absolute;top:1592px;width:284px;height:257px;background:var(--teal);border-radius:36px;padding:30px 24px 30px 26px;color:var(--white)}
.card-head{display:flex;align-items:center;gap:10px;font-family:"Barlow Condensed",sans-serif;font-weight:600;font-size:21px;margin-bottom:14px}
.card-icon{width:44px;height:44px;border-radius:50%;background:rgba(255,255,255,.25)}
.card p{font-size:13.8px;line-height:21px;letter-spacing:-.15px}
.card .more{display:inline-block;margin-top:10px;font-family:"Barlow Condensed",sans-serif;font-weight:600;font-size:15px;border-bottom:1px solid var(--white)}

.post{position:absolute;top:2134px;width:278px}
.post .thumb{height:189px;border-radius:8px}
.post .date{margin-top:12px;font-family:"Barlow Condensed",sans-serif;font-weight:500;font-size:13px;color:var(--teal)}
.post h3{font-family:"Barlow Condensed",sans-serif;font-weight:500;font-size:22px;color:var(--ink);margin-top:6px}
.post p{font-size:13.8px;line-height:22px;letter-spacing:-.15px;margin-top:6px}
.post .more{display:flex;align-items:center;gap:8px;margin-top:12px;font-family:"Barlow Condensed",sans-serif;font-weight:500;font-size:16px;color:var(--teal)}

.form-card{position:absolute;left:163px;top:2652px;width:655px;height:418px;background:var(--white);border-radius:20px;box-shadow:0 10px 40px rgba(20,40,80,.08)}
.field{position:absolute;left:34px;width:476px;border-bottom:1px solid #9aa3b0;font-size:12.5px;color:var(--ink)}
.contact-card{position:absolute;left:712px;top:2713px;width:324px;height:407px;background:var(--teal);border-radius:14px;padding:48px 20px;color:var(--white)}
.contact-card .row{display:flex;gap:12px;font-size:13.8px;line-height:23px;margin-top:16px}
.tab{position:absolute;height:14px;border-radius:7px}

.footer{position:absolute;left:0;top:3172px;width:1200px;height:464px;background:var(--navy);color:var(--white)}
.fnav{position:absolute;top:365px;left:0;width:1200px;display:flex;justify-content:center;gap:50px;font-family:"Barlow Condensed",sans-serif;font-weight:600;font-size:16px}
</style>
</head>
<body>

<!-- Hero -->
<section class="hero">
  <div class="hero-arc"></div>
  <div class="abs brand" style="left:163px;top:28px"><span class="brand-mark"></span>Laurent Dubreuil Conseil</div>
  <nav class="nav">
    <a class="active" style="left:0;top:0">Home</a>
    <a style="left:80px;top:0">About</a>
    <a style="left:162px;top:0">Services</a>
    <a style="left:258px;top:0">Blog</a>
    <a style="left:330px;top:0">Contact</a>
    <a class="phone" style="left:417px;top:0">
      <svg width="13" height="13" viewBox="0 0 24 24"><path fill="#0f8b96" d="M6.6 10.8a15 15 0 0 0 6.6 6.6l2.2-2.2c.3-.3.7-.4 1-.2 1.1.4 2.3.6 3.6.6.6 0 1 .4 1 1V20c0 .6-.4 1-1 1A17 17 0 0 1 3 4c0-.6.4-1 1-1h3.5c.6 0 1 .4 1 1 0 1.3.2 2.5.6 3.6.1.3 0 .7-.2 1z"/></svg>01 480 272 915
    </a>
  </nav>
  <div class="hero-art" role="img" aria-label="Isometric illustration of a monitor with a user profile, a padlock, a key and a smartphone"></div>
  <p class="abs accent" style="left:163px;top:208px;font-family:'Krona One',sans-serif;font-size:18px;font-style:italic;letter-spacing:1px">We Specialized in</p>
  <h1 class="abs display" style="left:163px;top:236px;font-size:33px;line-height:44px">Data privacy &amp;<br>Computer Science</h1>
  <a class="btn" style="left:163px;top:340px;width:150px;height:44px">Learn More</a>
  <div class="slider"><span class="accent" style="font-size:15px">01</span><span class="line"></span><span style="font-size:11px;color:var(--ink)">04</span></div>
</section>

<!-- Welcome -->
<section>
  <div class="photo" role="img" aria-label="Consultant working at a desktop computer in front of a teal frame" style="left:163px;top:627px;width:402px;height:318px;border-radius:30px;background:linear-gradient(135deg,#3b8d9a,#2b6f7c 50%,#5a6a78)"></div>
  <div class="stack" style="left:608px;top:632px;width:436px">
    <p class="accent" style="font-family:'Krona One',sans-serif;font-size:18px;letter-spacing:1px;line-height:24px">Welcome to</p>
    <h2 class="display" style="font-size:30px;line-height:38px;margin-top:4px">Laurent Dubreuil<br>Conseil</h2>
    <p class="copy" style="margin-top:13px">Nulla rhoncus scelerisque urna at sagittis. Nam non justo sit amet eros laoreet maximus sit amet et felis. Nullam id enim consequat, pharetra ligula non, falisis ligula. Sed et iaculis massa, vel elemtum nulla. Sed in magna fringilla molestie. Sed vehicula vel elit sit amet hendrerit. In sollicitudin, eros in tempor ullamcorper, tortor mauris tempor eros,</p>
    <a class="btn" style="width:150px;height:44px;margin-top:24px">Read More</a>
  </div>
</section>

<!-- Why choose us -->
<section class="band-soft" style="top:1011px;height:452px">
  <div class="stack" style="left:163px;top:92px;width:460px">
    <h2 class="display" style="font-size:31px;line-height:42px">Why Choose Us</h2>
    <p class="copy" style="margin-top:8px">Lorem ipsum dolor sit amet, consectetur adipiscing elit. Nullam pulvinar odio diam, efficitur convallis nulla ornare rutrum.</p>
    <ul class="ticks" style="margin-top:10px">
      <li><svg width="17" height="14" viewBox="0 0 17 14"><path d="M1.5 7.5l5 4.5 9-10" fill="none" stroke="#2aa34a" stroke-width="3" stroke-linecap="round" stroke-linejoin="round"/></svg>Lorem ipsum dolor sit amet, consectetur</li>
      <li><svg width="17" height="14" viewBox="0 0 17 14"><path d="M1.5 7.5l5 4.5 9-10" fill="none" stroke="#2aa34a" stroke-width="3" stroke-linecap="round" stroke-linejoin="round"/></svg>Quis ipsum suspendisse ultrices gravida.</li>
      <li><svg width="17" height="14" viewBox="0 0 17 14"><path d="M1.5 7.5l5 4.5 9-10" fill="none" stroke="#2aa34a" stroke-width="3" stroke-linecap="round" stroke-linejoin="round"/></svg>Risus commodo viverra maecenas</li>
    </ul>
    <a class="btn" style="width:150px;height:44px;margin-top:36px">Read More</a>
  </div>
  <div class="photo" role="img" aria-label="Person at a computer showing a privacy shield on screen" style="left:665px;top:51px;width:370px;height:354px;border-radius:40px;background:linear-gradient(140deg,#1e8b95,#6fa7b4 45%,#c9d3d8 70%,#2a7d88)"></div>
</section>

<!-- Services -->
<section>
  <h2 class="abs display" style="left:0;top:1530px;width:1200px;text-align:center;font-size:31px"><span class="accent">Our</span> Services</h2>
  <article class="card" style="left:165px">
    <div class="card-head"><span class="card-icon" role="img" aria-label="Security shield icon"></span>Security Services</div>
    <p>Lorem ipsum dolor sit amet, consectetur adipiscing elit, sed do eiusmod tempor incididunt ut labore et dolore magna aliqua.</p>
    <span class="more">Read More ▸</span>
  </article>
  <article class="card" style="left:459px">
    <div class="card-head"><span class="card-icon" role="img" aria-label="Protected document icon"></span>Data Privacy</div>
    <p>Lorem ipsum dolor sit amet, consectetur adipiscing elit, sed do eiusmod tempor incididunt ut labore et dolore magna aliqua.</p>
    <span class="more">Read More ▸</span>
  </article>
  <article class="card" style="left:753px">
    <div class="card-head"><span class="card-icon" role="img" aria-label="Computer analytics icon"></span>Computer Science</div>
    <p>Lorem ipsum dolor sit amet, consectetur adipiscing elit, sed do eiusmod tempor incididunt ut labore et dolore magna aliqua.</p>
    <span class="more">Read More ▸</span>
  </article>
  <a class="btn" style="left:525px;top:1872px;width:150px;height:44px;background:var(--white);color:var(--teal);border:1.5px solid var(--teal)">View All Services</a>
</section>

<!-- Blog -->
<section class="band-soft" style="top:1995px;height:585px">
  <h2 class="abs display" style="left:0;top:70px;width:1200px;text-align:center;font-size:31px"><span class="accent">Blog</span> &amp; Articles</h2>
  <svg class="abs" style="left:133px;top:224px" width="24" height="30" viewBox="0 0 24 30"><path d="M20 2L6 15l14 13" fill="none" stroke="#6b7583" stroke-width="1.8"/></svg>
  <svg class="abs" style="left:1038px;top:224px" width="24" height="30" viewBox="0 0 24 30"><path d="M4 2l14 13L4 28" fill="none" stroke="#0f8b96" stroke-width="1.8"/></svg>
</section>
<article class="post" style="left:163px">
  <div class="thumb" role="img" aria-label="Two people looking at code on several monitors" style="background:linear-gradient(135deg,#3a3b34,#1f5a3f 50%,#6b5a48)"></div>
  <p class="date">Feb 16, 2022</p>
  <h3>Nam condimentum pharetra</h3>
  <p>Lorem ipsum dolor sit amet, conctetur adipiscing elit, sed do eiusmod</p>
  <span class="more">Read More <svg width="16" height="10" viewBox="0 0 16 10"><path d="M0 5h14M10 1l4 4-4 4" fill="none" stroke="#0f8b96" stroke-width="1.5"/></svg></span>
</article>
<article class="post" style="left:461px">
  <div class="thumb" role="img" aria-label="Developer typing code on a keyboard at a bright desk" style="background:linear-gradient(135deg,#8e9aa5,#3d4650 50%,#c5ccd2)"></div>
  <p class="date">Feb 16, 2022</p>
  <h3>Nam condimentum pharetra</h3>
  <p>Lorem ipsum dolor sit amet, conctetur adipiscing elit, sed do eiusmod</p>
  <span class="more">Read More <svg width="16" height="10" viewBox="0 0 16 10"><path d="M0 5h14M10 1l4 4-4 4" fill="none" stroke="#0f8b96" stroke-width="1.5"/></svg></span>
</article>
<article class="post" style="left:758px">
  <div class="thumb" role="img" aria-label="Woman working on a laptop in a cafe" style="background:linear-gradient(135deg,#b88c6a,#d9c2b3 50%,#4e5660)"></div>
  <p class="date">Feb 16, 2022</p>
  <h3>Nam condimentum pharetra</h3>
  <p>Lorem ipsum dolor sit amet, conctetur adipiscing elit, sed do eiusmod</p>
  <span class="more">Read More <svg width="16" height="10" viewBox="0 0 16 10"><path d="M0 5h14M10 1l4 4-4 4" fill="none" stroke="#0f8b96" stroke-width="1.5"/></svg></span>
</article>

<!-- Contact -->
<section>
  <div class="abs" style="left:0;top:2580px;width:1200px;height:592px;background:linear-gradient(180deg,#ffffff,#f4f6fb)"></div>
  <span class="tab" style="left:113px;top:3012px;width:62px;background:var(--white)"></span>
  <span class="tab" style="left:135px;top:3034px;width:40px;background:var(--white)"></span>
  <div class="form-card">
    <h2 class="abs display" style="left:32px;top:40px;font-size:25px;line-height:34px">Send us A<br>Message</h2>
    <div class="field" style="top:132px;height:22px">Name</div>
    <div class="field" style="top:186px;height:28px">Email</div>
    <div class="field" style="top:235px;height:86px">Message</div>
    <a class="btn" style="left:380px;top:354px;width:134px;height:42px">Send To Us</a>
  </div>
  <span class="tab" style="left:1025px;top:2766px;width:37px;background:var(--teal)"></span>
  <span class="tab" style="left:1025px;top:2790px;width:25px;background:var(--teal)"></span>
  <span class="tab" style="left:1025px;top:3055px;width:25px;background:var(--teal)"></span>
  <span class="tab" style="left:1025px;top:3079px;width:40px;background:var(--teal)"></span>
  <div class="contact-card">
    <h2 class="display" style="color:var(--white);font-size:24px">Contact Us</h2>
    <p style="font-size:13.8px;line-height:23px;margin-top:8px">Pellentesque habitant morbi tristique senectus et netus et malesuada</p>
    <div class="row" style="margin-top:20px"><svg width="14" height="18" viewBox="0 0 24 30"><path fill="#fff" d="M12 0a10 10 0 0 0-10 10c0 7.5 10 20 10 20s10-12.5 10-20A10 10 0 0 0 12 0zm0 14a4 4 0 1 1 0-8 4 4 0 0 1 0 8z"/></svg><span>18 Rue Verte, Lyon,<br>France</span></div>
    <div class="row"><svg width="14" height="18" viewBox="0 0 24 24"><path fill="#fff" d="M2 5h20v14H2z"/><path d="M2 5l10 8 10-8" fill="none" stroke="#0f8b96" stroke-width="2"/></svg><span>info@laurentdubreuilconseil.com</span></div>
    <div class="row"><svg width="14" height="18" viewBox="0 0 24 24"><path fill="#fff" d="M6.6 10.8a15 15 0 0 0 6.6 6.6l2.2-2.2c.3-.3.7-.4 1-.2 1.1.4 2.3.6 3.6.6.6 0 1 .4 1 1V20c0 .6-.4 1-1 1A17 17 0 0 1 3 4c0-.6.4-1 1-1h3.5c.6 0 1 .4 1 1 0 1.3.2 2.5.6 3.6.1.3 0 .7-.2 1z"/></svg><span>01 480 272 915</span></div>
    <div style="display:flex;gap:14px;margin-top:22px;padding-left:10px">
      <span style="width:12px;height:12px;border-radius:50%;background:var(--white)"></span>
      <span style="width:12px;height:12px;border-radius:50%;background:var(--white)"></span>
      <span style="width:12px;height:12px;border-radius:50%;background:var(--white)"></span>
    </div>
  </div>
</section>

<!-- Footer -->
<footer class="footer">
  <h2 class="abs display" style="left:0;top:90px;width:1200px;text-align:center;color:var(--white);font-size:25px">Subscribe Our Newsletter</h2>
  <p class="abs" style="left:290px;top:124px;width:620px;text-align:center;font-size:13.8px;line-height:22px;color:#aab4c2">Lorem ipsum dolor sit amet, consectetur adipiscing elit. Mauris augunibh, viverra et enim ut, facilisis dapibus massa. pulvinar a</p>
  <div class="abs" style="left:385px;top:170px;width:431px;height:53px;background:var(--white);border-radius:6px">
    <span class="abs" style="left:20px;top:18px;font-size:12.5px;color:#7d8693">Enter Email Address</span>
    <a class="btn" style="left:308px;top:5px;width:117px;height:43px">Subscribe</a>
  </div>
  <div class="abs brand" style="left:0;top:300px;width:1200px;justify-content:center;color:var(--white)"><span class="brand-mark"></span>Laurent Dubreuil Conseil</div>
  <nav class="fnav"><span>Home</span><span>About</span><span>Services</span><span>Blog</span><span>Contact</span></nav>
  <div class="abs" style="left:163px;top:408px;width:874px;height:1px;background:#33455c"></div>
  <p class="abs cond" style="left:0;top:430px;width:1200px;text-align:center;font-weight:500;font-size:14px;color:#aab4c2">© 2022 <span class="accent">Laurent Dubreuil Conseil</span>. All right reserved</p>
</footer>

</body>
</html>
```